Bar and Grill looking or a Responsive Web design

New Bar and Grill in the Toronto area just opened up and is looking for a new wordpress website to start off his business.

Their business revolves around a homey family, upbeat atmosphere. His cuisine is gourmet pub style food. Speciality are home made burgers. 90 Seat restaurant in a very diverse and high density neighbourhood.

Looking for a responsive web design that will focus on a key feature pages.

Homepage
- Navigation is easy and simple, emphasize easy navigation in Mobile view.
- Contact information is a click or touch away

About Page

Menu Page
-Menu styling to be responsive. Very simple navigation through different menus and then menu would appear.

Gallery

Contact page
- Map (not googlesk)
- Contact Details
- Contact/Feedback form

They do have a logo and will be uploaded.

We are open to any designs, as well as designs based off templates that have already been created.

Target Market(s)

Target audience is the varied. They are in an area that's densely populated and very diverse. Looking for a crowd that appreciates a setting for sports, good gourmet pub styled food and a home styled restaurant.

Industry/Entity Type

Restaurant

Colors

Designer to choose colors to be used in the design.

Requirements
Must have
• Menus have to have responsive design for both mobile and tablet/desktop.
Nice to have
• Easy access contact button on mobile view. That way it will act like a webapp so that mobile devices can take advantage of quick touches to get in contact.

```html
<!DOCTYPE html>
<html lang="en">
<head>
<meta charset="utf-8">
<title>Maplecourt Bar &amp; Grill</title>
<link href="https://fonts.googleapis.com/css2?family=Merienda:wght@400;700&family=Didact+Gothic&display=swap" rel="stylesheet">
<style>
:root{
  --bar:#3d3220;
  --bar-line:#5a4c34;
  --cream:#faf6ec;
  --gold:#d4a64c;
  --gold-soft:#c9a062;
  --ink:#3e311f;
  --text:#6d604f;
  --muted:#8f8676;
  --white:#ffffff;
}
*{margin:0;padding:0;box-sizing:border-box}
html,body{width:840px;height:1200px;overflow:hidden}
body{background:var(--cream);font-family:"Didact Gothic",sans-serif;color:var(--text);position:relative}
.abs{position:absolute}
.topbar{left:0;top:0;width:840px;height:35px;background:var(--bar);border-bottom:2px solid var(--gold-soft)}
.topbar nav a{position:absolute;top:11px;font-family:"Merienda",cursive;font-size:9px;color:#efe6d2;text-decoration:none;letter-spacing:.5px}
.social{display:flex;gap:9px}
.social span{width:19px;height:19px;border-radius:50%;background:#4a4032;border:2px solid #cfc6b4;display:block}
.brand{left:320px;top:72px;width:200px;text-align:center;font-family:"Merienda",cursive;font-weight:700;font-size:30px;color:#8a6a42;letter-spacing:1px}
.call{right:51px;top:72px;font-size:12px;color:var(--ink);font-weight:bold}
.call em{font-style:normal;color:var(--gold);font-weight:normal}
.slider{left:52px;top:154px;width:737px;height:293px;background:var(--white);box-shadow:0 1px 2px rgba(0,0,0,.05)}
.slide{left:65px;top:164px;width:711px;height:272px;background:linear-gradient(100deg,#4a1622 0%,#6d2334 30%,#8b4a32 55%,#5b1420 70%,#9a6a45 100%)}
.caption{left:393px;top:386px;width:383px;height:50px;background:linear-gradient(90deg,rgba(150,110,40,.85),rgba(190,140,60,.8));font-family:"Merienda",cursive;font-weight:700;font-size:15px;color:var(--white);padding:13px 0 0 14px;letter-spacing:.6px}
.shadow{top:448px;height:4px;width:165px;border-radius:50%;background:radial-gradient(ellipse,rgba(0,0,0,.18),transparent 70%)}
.feature{width:234px}
.feature .photo{height:131px;background:var(--white);border:1px solid #e3dccb;padding:4px}
.feature .photo div{width:100%;height:100%}
.feature h3{font-family:"Merienda",cursive;font-size:10px;color:var(--ink);margin-top:14px}
.feature p{font-size:8.3px;line-height:12.3px;margin-top:8px;width:232px}
.divider{left:52px;top:780px;width:737px;height:2px}
.section-title{font-family:"Merienda",cursive;font-size:11px;color:var(--gold-soft)}
.thumbs{left:52px;top:834px;display:flex;gap:6px}
.thumbs div{width:87px;height:50px;background:var(--white);border:1px solid #e0d9c8;padding:3px}
.thumbs i{display:block;width:100%;height:100%}
.quote-mark{left:430px;top:838px;font-family:"Merienda",cursive;font-size:34px;color:var(--gold-soft);line-height:1}
.quote{left:469px;top:836px;width:320px;font-size:8.3px;line-height:12.3px;font-style:italic;color:var(--text)}
.author{right:51px;top:907px;font-family:"Merienda",cursive;font-size:8.5px;color:var(--gold-soft)}
.footer{left:0;top:953px;width:840px;height:247px;background:var(--bar);border-top:3px solid #574a33}
.footer h4{font-family:"Merienda",cursive;font-size:10px;color:var(--gold);font-weight:700}
.footer .line{font-size:8.3px;color:var(--muted);letter-spacing:.3px}
.footer .line b{font-weight:normal;color:#e9e1d0}
.hours{left:304px;top:1002px;font-size:8.3px;color:var(--muted);letter-spacing:.3px}
.hours div{display:flex;height:17.5px}
.hours span:first-child{width:132px}
.foot-social{left:52px;top:1080px;display:flex;gap:9px}
.foot-social span{width:19px;height:19px;border-radius:50%;border:1px solid #9a907f;background:#443a2a;display:block}
.bottom{left:0;top:1156px;width:840px;border-top:1px solid var(--bar-line)}
.copy{left:52px;top:1173px;font-size:8.3px;color:var(--muted);letter-spacing:.3px}
.bottom-nav a{position:absolute;top:1174px;font-size:8.3px;color:var(--muted);text-decoration:none;letter-spacing:.3px}
</style>
</head>
<body>

<header class="abs topbar">
  <nav>
    <a style="left:53px">Home</a>
    <a style="left:134px">About us</a>
    <a style="left:230px">Our menu</a>
    <a style="left:331px">Gallery</a>
    <a style="left:418px">Contact us</a>
  </nav>
</header>

<div class="abs social" style="left:53px;top:71px"><span></span><span></span><span></span><span></span></div>
<div class="abs brand">MAPLECOURT</div>
<div class="abs call">Call Us : <em>+000 000 000</em></div>

<section>
  <div class="abs slider"></div>
  <div class="abs slide" role="img" aria-label="Red wine in a glass beside dark grapes"></div>
  <svg class="abs" style="left:757px;top:167px" width="16" height="16" viewBox="0 0 16 16"><path d="M3 6a6 6 0 1 1 2 8" fill="none" stroke="#fff" stroke-width="1.6"/></svg>
  <div class="abs caption">We Serve Premium Wine !</div>
  <div class="abs shadow" style="left:133px"></div>
  <div class="abs shadow" style="left:548px"></div>
</section>

<section>
  <article class="abs feature" style="left:52px;top:497px">
    <div class="photo"><div role="img" aria-label="Group of friends toasting with bottles" style="background:linear-gradient(135deg,#5a3b2e,#c49a7e 50%,#3a3442)"></div></div>
    <h3>Prompt Services</h3>
    <p>Lorem ipsum dolor sit amo nsec tetuer adipisc ing eliraesent vestibulum molestie lacunean nonummyendrerit mauris. Phasellus porta. Fusce suscipit varius mi. Cum sociis natoque penatibus et magnis dis.</p>
  </article>
  <article class="abs feature" style="left:304px;top:497px">
    <div class="photo"><div role="img" aria-label="Two glasses of red wine with grapes" style="background:linear-gradient(180deg,#c8772e,#a85a22 55%,#3a2418)"></div></div>
    <h3>Premium Wines</h3>
    <p>Lorem ipsum dolor sit amo nsec tetuer adipisc ing eliraesent vestibulum molestie lacunean nonummyendrerit mauris. Phasellus porta. Fusce suscipit varius mi. Cum sociis natoque penatibus et magnis dis.</p>
  </article>
  <article class="abs feature" style="left:556px;top:497px">
    <div class="photo"><div role="img" aria-label="Home made burger with cheese and tomato" style="background:linear-gradient(180deg,#1a1a1a,#c98a45 35%,#d6402a 55%,#5b8a2c 75%,#e9e0d0)"></div></div>
    <h3>Best Foods</h3>
    <p>Lorem ipsum dolor sit amo nsec tetuer adipisc ing eliraesent vestibulum molestie lacunean nonummyendrerit mauris. Phasellus porta. Fusce suscipit varius mi. Cum sociis natoque penatibus et magnis dis.</p>
  </article>
</section>

<svg class="abs" style="left:52px;top:772px" width="737" height="16" viewBox="0 0 737 16">
  <circle cx="4" cy="8" r="3" fill="none" stroke="#e0cfa8"/>
  <circle cx="733" cy="8" r="3" fill="none" stroke="#e0cfa8"/>
  <line x1="7" y1="8" x2="360" y2="8" stroke="#e6d8b8"/>
  <line x1="377" y1="8" x2="730" y2="8" stroke="#e6d8b8"/>
  <path d="M364 2h10l-5 7z M369 9v5 M366 14h6" fill="none" stroke="#d4a64c" stroke-width="1.2"/>
</svg>

<section>
  <h2 class="abs section-title" style="left:52px;top:811px">Today's Special</h2>
  <div class="abs thumbs">
    <div><i role="img" aria-label="Chocolate cake with berries" style="background:linear-gradient(180deg,#e8e2d8,#5a3420 60%,#a0283a)"></i></div>
    <div><i role="img" aria-label="Chef preparing pastry" style="background:linear-gradient(180deg,#c87b43,#e0a040 60%,#f1e6d6)"></i></div>
    <div><i role="img" aria-label="Chocolate cake with berries" style="background:linear-gradient(180deg,#e8e2d8,#5a3420 60%,#a0283a)"></i></div>
    <div><i role="img" aria-label="Plated dessert with orange sauce" style="background:linear-gradient(135deg,#fff,#f0c89a 50%,#f08a30)"></i></div>
  </div>

  <h2 class="abs section-title" style="left:430px;top:811px">Testimonials</h2>
  <div class="abs quote-mark">&ldquo;</div>
  <p class="abs quote">Fusce sscipit varius m sociis natoque penatibet ma rturient montes naetu ridiculu msulla dui. Fusce feulesuada odio. Morbi nunc odio grvda aursu ctus a lorem. Maecenas trque orci ac tricies pharetra. Fusce sscipit varius m sociis natoque penatibet ma rturient montes naetu ridiculu msulla dui. Fusce feulesuada odio. Morbi nunc odio.</p>
  <div class="abs author">-Evelyn Marsh</div>
</section>

<footer>
  <div class="abs footer"></div>
  <h4 class="abs" style="left:52px;top:981px;font-family:'Merienda',cursive;font-size:10px;color:var(--gold)">Visit Us</h4>
  <div class="abs footer-lines" style="left:52px;top:1004px">
    <p class="line" style="height:19.6px;font-size:8.3px;color:var(--muted)">Some Street Road.</p>
    <p class="line" style="height:19.6px;font-size:8.3px;color:var(--muted)">Torronto, D04 89 CA.</p>
    <p class="line" style="height:19.6px;font-size:8.3px;color:var(--muted)">Telephone: +0 000 000 0000</p>
    <p class="line" style="height:19.6px;font-size:8.3px;color:var(--muted)">E-mail:<b style="font-weight:normal;color:#e9e1d0">info@maplecourt.com</b></p>
  </div>
  <div class="abs foot-social"><span></span><span></span><span></span><span></span></div>

  <h4 class="abs" style="left:304px;top:981px;font-family:'Merienda',cursive;font-size:10px;color:var(--gold)">Working Hours</h4>
  <div class="abs hours">
    <div><span>Monday</span><span>10:30am - 11:30pm</span></div>
    <div><span>Tuesday</span><span>10:30am - 11:30pm</span></div>
    <div><span>Wednesday</span><span>10:30am - 11:30pm</span></div>
    <div><span>Thursday</span><span>10:30am - 11:30pm</span></div>
    <div><span>Friday</span><span>10:30am - 11:30pm</span></div>
    <div><span>Saturday</span><span>10:30am - 11:30pm</span></div>
    <div><span>Sunday</span><span>10:30am - 11:30pm</span></div>
  </div>

  <div class="abs bottom"></div>
  <p class="abs copy">&copy; 2013-14 Maplecourt Bar &amp; Grill,All Rights Reserved.</p>
  <nav class="bottom-nav">
    <a style="left:483px">Home</a>
    <a style="left:539px">About us</a>
    <a style="left:608px">Our menu</a>
    <a style="left:681px">Gallery</a>
    <a style="left:743px">Contact us</a>
  </nav>
</footer>

</body>
</html>
```